Kettle Lane Kitchen February contest

The website slider is 990 X 225 pixels to fit in with this website www.kettlelanekitchen.com.au
We would love a fun, lively, food-oriented slider created for Kettle Lane Kitchen website. Kettle Lane Kitchen is a central place where people who love food, cooking for their family and friends, and sharing recipes can hang out. We'd like the sliders to be simple, bright and to entice people to click on the link.
The banner ad needs to feature the Varnholt mixer, and to use a colour scheme that also works with the existing website. There's a blog with more information on the Varnholt mixer here http://kettlelanekitchen.com.au/uncategorized/upload-a-recipe-in-february-to-be-in-the-running-to-win-a-varnholt-mixer/
A slider in December was used to promote a similar competition which I will upload as inspiration, along with the image of the Varnholt mixer to use.
Main text: Add your best recipe by February 28 to win!
Smaller text: Best recipe as chosen by Kettle Lane Kitchen editors will win a Varnholt mixer worth $699.
Target Market(s)
Food lovers - home cooks and food bloggers. Mainly women, 30+
Industry/Entity Type
Chef

```html
<!DOCTYPE html>
<html lang="en">
<head>
<meta charset="utf-8">
<title>Kettle Lane Kitchen – February Contest</title>
<link rel="stylesheet" href="https://fonts.googleapis.com/css2?family=Anton&family=Kalam:wght@400;700&family=Roboto:ital,wght@0,400;0,700;1,400&display=swap">
<style>
  :root {
    --page-bg: #efe5d7;
    --white: #ffffff;
    --accent: #df5229;
    --accent-dark: #c8461f;
    --brown: #6a4134;
    --cream: #f6eddb;
    --ink: #3a3330;
    --ink-soft: #555049;
    --logo-ink: #4a3028;
    --search-bg: #fbefe4;
    --search-line: #ead7c6;
    --search-icon: #f3b86e;
  }
  * { box-sizing: border-box; margin: 0; padding: 0; }
  html, body { width: 1200px; height: 513px; overflow: hidden; }
  body {
    position: relative;
    background: var(--page-bg);
    font-family: "Roboto", Arial, sans-serif;
    color: var(--ink);
  }
  .abs { position: absolute; }

  .account-links {
    left: 933px; top: 0; width: 108px; height: 25px;
    background: var(--white); border-radius: 0 0 4px 4px;
    font-size: 12px; color: var(--accent);
    display: flex; align-items: center; justify-content: center; gap: 10px;
  }

  .brand-badge {
    left: 157px; top: -18px; width: 160px; height: 160px;
    border-radius: 50%; background: var(--white);
    box-shadow: 0 1px 3px rgba(0,0,0,.15);
    display: flex; align-items: center; justify-content: center;
    z-index: 3;
  }
  .brand-name {
    font-family: "Roboto", Arial, sans-serif; font-weight: 700;
    font-size: 22px; line-height: 25px; color: var(--logo-ink);
    text-align: center; margin-top: 18px;
  }

  .community-call {
    left: 458px; top: 28px;
    font-family: "Kalam", cursive; font-size: 24px; color: var(--ink-soft);
  }
  .community-arrow { left: 772px; top: 34px; }

  .main-nav {
    left: 323px; top: 89px; width: 272px; height: 36px;
    background: var(--white);
    display: flex; align-items: center; gap: 18px; padding-left: 22px;
    font-size: 11px; font-weight: 700; color: var(--ink-soft);
  }
  .main-nav span { display: flex; align-items: center; gap: 4px; }

  .site-nav {
    left: 595px; top: 89px; width: 446px; height: 36px;
    background: var(--accent); border-radius: 0 4px 0 0;
    display: flex; align-items: center; padding-left: 29px; gap: 8px;
    font-size: 11px; font-weight: 700; color: var(--white);
  }
  .site-nav .dot { width: 4px; height: 4px; border-radius: 50%; background: var(--white); }

  .promo-slider {
    left: 157px; top: 127px; width: 886px; height: 203px;
    background: var(--brown); overflow: hidden;
    box-shadow: 0 1px 3px rgba(0,0,0,.25);
  }
  .promo-headline {
    left: 16px; top: 24px;
    font-family: "Anton", Impact, sans-serif; font-size: 33px; line-height: 41px;
    color: var(--cream); letter-spacing: .3px;
  }
  .mixer-photo {
    left: 195px; top: 50px; width: 190px; height: 140px;
    border-radius: 40px 20px 10px 10px;
    background: linear-gradient(120deg, #e9eef0 0%, #cfd8dc 35%, #3cc1d6 55%, #9fdbe6 80%, #d9dfe1 100%);
  }
  .food-photo {
    left: 391px; top: 0; width: 495px; height: 203px;
    background: linear-gradient(100deg, #8f4a22 0%, #c8742f 25%, #6f9a42 40%, #e1b24c 62%, #c96a2c 80%, #7a3f1c 100%);
  }
  .prize-badge {
    left: 560px; top: 80px; width: 130px; height: 122px;
    background: var(--cream); border: 2px solid var(--accent);
    border-radius: 12px; transform: rotate(-14deg);
    display: flex; flex-direction: column; align-items: center; justify-content: center;
    text-align: center; color: var(--ink); font-weight: 700;
  }
  .prize-badge .small { font-size: 9.5px; line-height: 11px; }
  .prize-badge .win { font-family: "Anton", Impact, sans-serif; font-size: 20px; line-height: 22px; font-weight: 400; }
  .prize-badge .item { font-size: 15px; line-height: 17px; }

  .content-area {
    left: 157px; top: 333px; width: 884px; height: 180px;
    background: var(--white);
  }
  .section-title {
    display: flex; align-items: center; gap: 9px;
    font-size: 19px; color: var(--ink);
  }
  .featured-title { left: 168px; top: 351px; }
  .rated-title { left: 765px; top: 414px; }

  .recipe-photo { top: 391px; width: 179px; height: 122px; }
  .photo-lasagne { left: 167px; background: radial-gradient(circle at 50% 70%, #c5502a 0%, #e07a3a 30%, #f4f0ea 55%, #5a3b2a 100%); }
  .photo-spaghetti { left: 363px; background: radial-gradient(circle at 50% 70%, #b0512c 0%, #e8c98a 35%, #f3efe8 55%, #7a4a3c 100%); }
  .photo-soup { left: 560px; background: radial-gradient(circle at 50% 70%, #9b9a3a 0%, #c7a85a 35%, #f2f0ea 55%, #b7b3a6 100%); }

  .search-box {
    left: 765px; top: 343px; width: 264px; height: 34px;
    background: var(--search-bg); border: 1px solid var(--search-line); border-radius: 3px;
    padding-left: 10px; display: flex; align-items: center; justify-content: space-between; padding-right: 10px;
    font-size: 13px; font-style: italic; color: var(--ink);
  }
  .search-scope {
    left: 911px; top: 382px; font-size: 12px; color: var(--ink-soft);
    display: flex; align-items: center; gap: 4px;
  }
  .radio { width: 11px; height: 11px; border: 1px solid #777; border-radius: 50%; display: inline-flex; align-items: center; justify-content: center; margin-right: 8px; }
  .radio.on::after { content: ""; width: 5px; height: 5px; border-radius: 50%; background: #333; }

  .rated-photo {
    left: 765px; top: 454px; width: 119px; height: 59px;
    background: linear-gradient(110deg, #f4efe4 0%, #e9dcb8 40%, #c9322c 60%, #f1e9d8 80%, #b9c67a 100%);
  }
  .rank-chip {
    left: 753px; top: 479px; width: 28px; height: 28px; border-radius: 50%;
    background: var(--white); font-size: 11px; display: flex; align-items: center; justify-content: flex-end; padding-right: 9px;
  }
  .rated-text { left: 893px; top: 455px; width: 145px; font-size: 12px; line-height: 17px; color: var(--ink); }
  .rated-author { left: 893px; top: 506px; font-size: 12px; font-weight: 700; color: var(--accent-dark); }
</style>
</head>
<body>

  <div class="abs account-links"><span>Register</span><span>Login</span></div>

  <div class="abs brand-badge"><div class="brand-name">Kettle<br>Lane<br>Kitchen</div></div>

  <div class="abs community-call">Join the community now!</div>
  <svg class="abs community-arrow" width="44" height="22" viewBox="0 0 44 22" aria-hidden="true">
    <path d="M3 18 Q20 6 38 8" fill="none" stroke="var(--accent)" stroke-width="2" stroke-linecap="round"/>
    <path d="M31 3 L39 8 L32 13" fill="none" stroke="var(--accent)" stroke-width="2" stroke-linecap="round" stroke-linejoin="round"/>
  </svg>

  <nav class="abs main-nav">
    <span>
      <svg width="18" height="12" viewBox="0 0 18 12" aria-hidden="true"><path d="M1 5 H15 Q14 11 8 11 Q2 11 1 5Z" fill="var(--accent)"/><path d="M10 5 L17 1" stroke="var(--accent)" stroke-width="1.6"/></svg>
      Recipes
    </span>
    <span>
      <svg width="16" height="14" viewBox="0 0 16 14" aria-hidden="true"><circle cx="5" cy="5" r="4" fill="var(--accent)"/><circle cx="11" cy="5" r="4" fill="var(--accent)"/><circle cx="8" cy="3.5" r="3.5" fill="var(--accent)"/><rect x="3" y="7" width="10" height="6" rx="1" fill="var(--accent)"/></svg>
      Chefs
    </span>
    <span>
      <svg width="16" height="14" viewBox="0 0 16 14" aria-hidden="true"><ellipse cx="8" cy="10" rx="4" ry="3.5" fill="var(--accent)"/><circle cx="3" cy="6" r="2" fill="var(--accent)"/><circle cx="6" cy="2.5" r="2" fill="var(--accent)"/><circle cx="10" cy="2.5" r="2" fill="var(--accent)"/><circle cx="13" cy="6" r="2" fill="var(--accent)"/></svg>
      Mentors
    </span>
  </nav>

  <nav class="abs site-nav">
    <span>Upload your recipe</span><i class="dot"></i>
    <span>Prizes</span><i class="dot"></i>
    <span>About</span><i class="dot"></i>
    <span>FAQs</span><i class="dot"></i>
    <span>Contact</span><i class="dot"></i>
    <span>Blog</span>
  </nav>

  <section class="abs promo-slider">
    <h1 class="abs promo-headline">Add Your Best<br>Recipe by<br>February 28<br>&nbsp;to Win!</h1>
    <div class="abs mixer-photo" role="img" aria-label="Photo of a turquoise and white Varnholt stand mixer with steel bowl"></div>
    <div class="abs food-photo" role="img" aria-label="Photo of roast chicken drumsticks, spiced rice and a curry in a copper bowl"></div>
    <div class="abs prize-badge">
      <span class="small">Best recipe<br>as chosen by Kettle Lane<br>Kitchen editors will</span>
      <span class="win">WIN</span>
      <span class="item">a Varnholt Mixer<br>worth $699</span>
    </div>
  </section>

  <div class="abs content-area"></div>

  <h2 class="abs section-title featured-title">
    <svg width="20" height="14" viewBox="0 0 20 14" aria-hidden="true"><path d="M1 6 H16 Q15 13 8.5 13 Q2 13 1 6Z" fill="var(--accent)"/><path d="M11 6 L19 1" stroke="var(--accent)" stroke-width="1.8"/></svg>
    <span style="font-weight:400">Featured Recipes</span>
  </h2>

  <div class="abs recipe-photo photo-lasagne" role="img" aria-label="Photo of a plated vegetable lasagne"></div>
  <div class="abs recipe-photo photo-spaghetti" role="img" aria-label="Photo of spaghetti bolognese topped with grated cheese"></div>
  <div class="abs recipe-photo photo-soup" role="img" aria-label="Photo of a bowl of vegetable soup"></div>

  <div class="abs search-box">
    <span>search</span>
    <svg width="20" height="20" viewBox="0 0 20 20" aria-hidden="true"><circle cx="8" cy="8" r="6" fill="none" stroke="var(--search-icon)" stroke-width="2.5"/><path d="M12.5 12.5 L18 18" stroke="var(--search-icon)" stroke-width="3" stroke-linecap="round"/></svg>
  </div>
  <div class="abs search-scope">
    Recipes <i class="radio on"></i> Chefs <i class="radio"></i>
  </div>

  <h2 class="abs section-title rated-title">
    <svg width="20" height="14" viewBox="0 0 20 14" aria-hidden="true"><path d="M1 6 H16 Q15 13 8.5 13 Q2 13 1 6Z" fill="var(--accent)"/><path d="M11 6 L19 1" stroke="var(--accent)" stroke-width="1.8"/></svg>
    <span style="font-weight:400">Highest Rated Recipes</span>
  </h2>

  <div class="abs rated-photo" role="img" aria-label="Photo of white chocolate parfait with strawberries"></div>
  <div class="abs rank-chip">1</div>
  <p class="abs rated-text">White Chocolate Parfait W/ Lemon Curd and Short ..</p>
  <p class="abs rated-author">By Mira Holt</p>

</body>
</html>
```